Business Card Design

VEGETABLE FARMING OPERATION PRIMARY CROPS SPINACH,SPRING MIX, HEAD LETTUCE, ROMAINE, BRUSSEL SPROUTS, KESTREL STEM GREENS BROCCOLI CAULIFLOWER CELERY NEED A Business card THAT REPRESENTS SOME OF THOSE CROPS AY IDEAS WELCOME..

The business is vegetable farming spinach spring mix head lettuce romaine broccoli brussel sprouts celery carrots target audience is potential shippers of products week spring mix spinach harvesting as well. I colors in mind just need a card that's original

Industry/Entity Type

Farming

Contact Information for Business Card

R&T FARMS LLC WILLOWDALE FARMS LLC

```html
<!DOCTYPE html>
<html lang="en">
<head>
<meta charset="utf-8">
<title>Business Card – Vegetable Farming Operation</title>
<link href="https://fonts.googleapis.com/css2?family=Roboto+Condensed:wght@700&display=swap" rel="stylesheet">
<style>
  :root {
    --backdrop: #0f2627;
    --card-white: #ffffff;
    --lime: #8cff14;
    --lime-edge: #b4ec1c;
    --lime-text: #93e82a;
    --veg-pale: #e6f5d6;
    --veg-light: #bfe69a;
    --veg-mid: #7fcf4a;
    --text-on-lime: #ffffff;
  }
  * { margin: 0; padding: 0; box-sizing: border-box; }
  html, body {
    width: 1200px;
    height: 877px;
    overflow: hidden;
    background: var(--backdrop);
  }
  .canvas {
    position: relative;
    width: 1200px;
    height: 877px;
    background: var(--backdrop);
  }
  .business-card {
    position: absolute;
    left: 280px;
    top: 234px;
    width: 661px;
    height: 352px;
    border-radius: 18px;
    overflow: hidden;
    background: var(--card-white);
    font-family: "Roboto Condensed", "Arial Narrow", sans-serif;
    font-weight: 700;
  }
  .crop-illustration {
    position: absolute;
    left: 58px;
    top: 78px;
    width: 216px;
    height: 142px;
    border-radius: 28px;
    background: linear-gradient(135deg, var(--veg-light) 0%, var(--veg-mid) 45%, var(--veg-pale) 100%);
  }
  .tagline {
    position: absolute;
    left: 20px;
    top: 233px;
    width: 286px;
    text-align: center;
    color: var(--lime-text);
    font-size: 20px;
    line-height: 36px;
    letter-spacing: 1px;
  }
  .panel-edge {
    position: absolute;
    left: 320px;
    top: 0;
    width: 341px;
    height: 100%;
    background: var(--lime-edge);
    border-radius: 24px 0 0 24px;
  }
  .panel-main {
    position: absolute;
    left: 328px;
    top: 0;
    width: 333px;
    height: 100%;
    background: var(--lime);
    border-radius: 24px 0 0 24px;
  }
  .company-list {
    position: absolute;
    top: 114px;
    width: 100%;
    list-style: none;
    text-align: center;
    color: var(--text-on-lime);
    font-size: 23px;
    line-height: 36px;
    letter-spacing: 1px;
  }
</style>
</head>
<body>
<main class="canvas">
  <section class="business-card">
    <div class="crop-illustration" role="img" aria-label="Illustration of vegetables: celery, broccoli, cauliflower, cabbage and lettuce"></div>
    <p class="tagline">VEGETABLE FARMING<br>OPERATION</p>
    <div class="panel-edge"></div>
    <div class="panel-main">
      <ul class="company-list">
        <li>R&amp;T FARMS LLC</li>
        <li>WILLOWDALE FARMS LLC</li>
      </ul>
    </div>
  </section>
</main>
</body>
</html>
```